Redesign My Travel Agency Agreements

I need my reservation request forms redesigned into a professional contract. This is a travel agency contract. Just needs to look professional. PDF format please. See attached
Target Market(s)
travel agencies and travelers
Industry/Entity Type
Travel Agency
Font styles to use
Other font styles liked:
- open
Requirements
Must have
- I need my reservation request forms redesigned into a professional contract. This is a travel agency contract. Just needs to look professional. PDF format please. See attached
Nice to have
Should not have

```html
<!DOCTYPE html>
<html lang="en">
<head>
<meta charset="utf-8">
<title>Reservation Request Terms – Page 2</title>
<link href="https://fonts.googleapis.com/css2?family=Arimo:ital,wght@0,400;0,700;1,400;1,700&display=swap" rel="stylesheet">
<style>
  :root {
    --brand-blue: #005b8f;
    --ink: #1f1f1f;
    --paper: #ffffff;
    --rule: #333333;
  }
  * { box-sizing: border-box; margin: 0; padding: 0; }
  html, body { width: 927px; height: 1200px; overflow: hidden; background: var(--paper); }
  body { font-family: "Arimo", Arial, sans-serif; color: var(--ink); position: relative; }

  .masthead {
    position: absolute; left: 0; top: 0; width: 927px; height: 162px;
    background: var(--brand-blue); color: var(--paper);
  }
  .masthead__brand {
    position: absolute; left: 55px; top: 58px;
    font-size: 22px; font-weight: 700; letter-spacing: 0.5px; line-height: 1.3;
    text-transform: uppercase;
  }
  .masthead__brand span { display: block; }
  .masthead__address {
    position: absolute; right: 55px; top: 51px; text-align: right;
    font-size: 14.3px; font-weight: 700; line-height: 18.1px;
  }

  .terms {
    position: absolute; left: 55px; top: 199px; width: 819px;
    font-size: 13.2px; line-height: 16.3px;
  }
  .terms p { margin-bottom: 16.8px; }
  .terms strong { font-weight: 700; }
  .terms h2 {
    font-size: 17.6px; font-weight: 700; line-height: 20px;
    margin-top: 2px; margin-bottom: 6px;
  }

  .signoff { position: absolute; left: 55px; width: 817px; font-size: 13.2px; font-weight: 700; display: flex; align-items: flex-end; }
  .signoff--name { top: 1081px; }
  .signoff--agree { top: 1115px; }
  .signoff__line { flex: 1; border-bottom: 1px solid var(--rule); height: 13px; margin-left: 4px; }
  .signoff__line--short { flex: 0 0 137px; }
  .signoff__gap { margin-left: 4px; }

  .page-footer {
    position: absolute; right: 54px; top: 1142px;
    font-size: 10px; font-style: italic;
  }
  .page-footer b { font-weight: 700; }
</style>
</head>
<body>
  <header class="masthead">
    <div class="masthead__brand">
      <span>Harbor Point Travel</span>
      <span style="font-size:14px;letter-spacing:1px;">Reservation Services</span>
    </div>
    <address class="masthead__address" style="font-style:normal;">
      Harbor Point Travel<br>
      48 Linden Avenue<br>
      Suite 310<br>
      Portland, ME 04101
    </address>
  </header>

  <main class="terms">
    <p>Reservation Request Form By Date printed on the first page of this reservation request form, your reservation request will become null void. We typically start searching inventory within 30 days of your requested arrival dates since this is when we have the most excess inventory available to us. We will notify you no later than 21-14 days prior to one of your requested travel dates by phone, email or first class mail with a confirmation or status update. If we do not have available inventory during any of your requested travel dates we will notify you by email offering you to resubmit your reservation request form for additional travel dates. The Booking Desk reserves the right to place you in the vicinity within a 25-mile radius of your destination of choice. By submitting your reservation request form you are authorizing us to book any one of your requests.</p>

    <p><strong>Travel Window:</strong> The “Travel Must Be Completed By” date is printed on the first page of this reservation request form.</p>

    <p><strong>Confirmation:</strong> When we book your trip we will contact you by email, online status, phone or by First-Class mail to let you know which departure date you received. Reservation is guaranteed for arrival on the confirmed check-in date &amp; time only. If you do not check-in on time the remaining portion of your reservation will be cancelled and you will not be entitled to a refund. Some cruise ships may apply additional charges that are not included in your reservation such as gratuity, taxes, maid fees, etc. You will be required to pay any such fees directly to the cruise ship (usually upon check-in).</p>

    <p><strong>Cancellations:</strong> If you cancel after your reservation is booked you will forfeit your room deposit plus any other fees you paid for the room. ALL BOOKINGS ARE FINAL and cannot be canceled, refunded, changed, exchanged or transferred. If you decide to cancel this reservation request before we purchase your accommodations, we will refund your fees minus the reservation guarantee deposit.</p>

    <h2>TRAVEL DOCUMENTS</h2>
    <p>You will need a valid passport to check in on the cruise ship. The Cruise ship requires a credit card imprint or a cash deposit to guarantee incidental charges (phone calls, room service, parking, resort fees, energy charges, etc.) that you may incur while staying on the ship. Should you have a special request, please contact the ship directly after your reservation is booked to coordinate your arrangements. You may incur additional fees for special arrangements if applicable.</p>

    <p><strong>Usage Limitations:</strong> You may not use this reservation request form in conjunction with any other travel offer. Only one reservation request form per household may be used within a 12-month period. It is nontransferable and may only be used by the original recipient. This reservation request form is not intended for conventions or group travel. 7 days before and 7 days after a Major Holiday are usually not available with this offer. Offer is invalid if incomplete, illegible or altered. This reservation request form is invalid if bartered or sold to the recipient. Expired reservation request forms can be renewed for a $29 surcharge. If lost or stolen, this reservation request form can be reinstated for a $29 surcharge.</p>

    <p><strong>Fulfillment:</strong> This reservation request form is administered and fulfilled by The Booking Desk. The Booking Desk will arrange hotel accommodations acting as an agent for hotels and/or other Travel Agencies. The Booking Desk will process all fees associated. The Booking Desk assumes no responsibility for loss, delay, accident, injury, or damage to persons, property or any liability whatsoever arising from or in conjunction with services provided. The Booking Desk reserves the right to substitute the components of the offered vacation and vary the itinerary should circumstances so require; destinations subject to change at any time. All federal, state and local laws apply. This offer does not include food, transportation, tips, telephone calls, or items of a personal nature. The Booking Desk reserves the right to offer you alternative itinerary if there is no availability during your requested travel dates. The Booking Desk reserves the right to book any of your date and destination combination choices. Traveler does not get to choose their cruise ship.</p>

    <p><strong>State Disclosures:</strong> This reservation request form is not valid where restricted or prohibited by law. “This contract is for the purchase of a vacation reservation request form and puts all assignees on notice of the consumer’s right to cancel under section 559.33, Florida Statute.”</p>

    <p><strong>Bound By Terms:</strong> By submitting all the attached reservation request form to The Booking Desk, the traveler consents to be bound by all the terms and provisions contained within the offer. The terms of the travel offer cannot be altered or amended except with the express written consent of an authorized officer of The Booking Desk.</p>
  </main>

  <div class="signoff signoff--name">Name:<span class="signoff__line"></span></div>
  <div class="signoff signoff--agree">I AGREE TO THE TERMS AND CONDITIONS:<span class="signoff__line"></span><span class="signoff__gap">DATE/TIME STAMP:</span><span class="signoff__line signoff__line--short"></span></div>

  <footer class="page-footer"><b>2 Night Bahama Cruise</b> - Page 2/3</footer>
</body>
</html>
```